Hockey Habits Poster Board for a Girls Youth Hockey Team

I'd like to have a (2) sided poster board created for our hockey team. The poster board will be 2'x4'. There are (4) different types of team play as follows:

Offense w/Puck - You have the puck and your team is on offense
-------------
Offense wo/Puck - You do not have the puck but your teammate does
-------------
Defense on/Puck - Your opponent has the puck and you are the closest defender from your team to the opponent with the puck
-------------
Defense away/Puck - Your opponent has the puck and you are not the closes defender from your team to the opponent with the puck
--------------
Individual habits are what we want every player to have regardless of the team situation. I think I'd like to have the individual habits on both sides of the poster board.

I'm open to ideas but I thought it would be cool to have a hockey rink in the background. This is also for a girls hockey team so if you are going to use a hockey player - please make sure the player is female.

Target Market(s)

Youth Hockey

Industry/Entity Type

Youth Sports - Hockey

Font styles to use
Serif
Sans Serif

Colors
0054AA
0677BA
7BADD7
CADEEF
E8F1F8
00AB8E
00BBA5
67D7C9
C6EFE9
E9F9F6

Requirements
Must have
• All of the individual habits on both sides. All the defensive habits on one side and the offensive habits on the other side.
Nice to have
• I'd like to see an image of a hockey rink on both sides of the poster as well as a female hockey player
Should not have
• boys

```html
<!DOCTYPE html>
<html lang="en">
<head>
<meta charset="utf-8">
<title>Hockey Habits Offense</title>
<link rel="stylesheet" href="https://fonts.googleapis.com/css2?family=Graduate&family=Poppins:ital,wght@0,600;1,400&display=swap">
<style>
  :root {
    --page: #f1f1f1;
    --arena-dark: #0b0f1e;
    --arena-mid: #2a3350;
    --ice: #c9ced8;
    --ice-light: #e6e8ee;
    --panel: rgba(236, 237, 240, 0.88);
    --stripe: rgba(255, 255, 255, 0.85);
    --red: #9e1a32;
    --orange: #d2600f;
    --yellow: #dfb015;
    --green: #5aa622;
    --label: #2a2a2a;
    --cell: #4a4a4a;
    --white: #ffffff;
  }
  * { margin: 0; padding: 0; box-sizing: border-box; }
  html, body { width: 985px; height: 1200px; overflow: hidden; background: var(--page); }
  .poster {
    position: absolute; left: 20px; top: 364px; width: 945px; height: 472px;
    overflow: hidden; box-shadow: 0 6px 14px rgba(0,0,0,0.35);
  }
  .rink-backdrop {
    position: absolute; inset: 0;
    background: linear-gradient(180deg, var(--arena-dark) 0%, var(--arena-mid) 38%, #8e96ab 55%, var(--ice) 72%, var(--ice-light) 100%);
  }
  .panel {
    position: absolute; left: 150px; top: 38px; width: 650px; height: 434px;
    background: var(--panel); border-radius: 14px 14px 0 0;
  }
  .title-band {
    position: absolute; left: 192px; top: 0; width: 562px; height: 56px;
    background: var(--red);
    clip-path: polygon(0 0, 100% 0, 94% 100%, 6% 100%);
    display: flex; align-items: center; justify-content: center;
  }
  .title-band h1 {
    font-family: "Graduate", serif; font-weight: 400; font-size: 33px;
    color: var(--white); letter-spacing: 1px;
  }
  .player {
    position: absolute;
  }
  .player--left {
    left: 0; top: 130px; width: 220px; height: 342px;
    background: linear-gradient(180deg, #2b2b30 0%, #d9dbe0 35%, #f2f2f4 70%, #1d1f26 100%);
    border-radius: 90px 90px 0 0;
  }
  .player--right {
    left: 690px; top: 50px; width: 255px; height: 422px;
    background: linear-gradient(180deg, #15161c 0%, #1f4fb0 30%, #1f4fb0 55%, #1a1a1f 80%, #2a2a30 100%);
    border-radius: 110px 60px 0 0;
  }
  .habits { position: absolute; left: 265px; width: 414px; }
  .habits--individual { top: 70px; }
  .habits--with-puck { top: 230px; }
  .habits--without-puck { top: 364px; }
  .grid {
    display: grid; grid-template-columns: 97px 103px 100px 114px;
  }
  .head { margin-bottom: 3px; }
  .tag {
    height: 19px; margin-right: 6px;
    clip-path: polygon(0 0, 100% 0, 96% 100%, 0 100%);
    display: flex; align-items: center; justify-content: center;
    font-family: "Graduate", serif; color: var(--white); font-size: 12px;
  }
  .tag--section { background: var(--red); font-size: 11px; }
  .tag--section.small { font-size: 7.5px; }
  .tag--average { background: var(--orange); }
  .tag--good { background: var(--yellow); }
  .tag--great { background: var(--green); }
  .row { min-height: 20.5px; align-items: center; padding: 1px 0; }
  .row:nth-child(odd) { background: var(--stripe); }
  .row--tight { min-height: 18.5px; }
  .label {
    font-family: "Poppins", sans-serif; font-weight: 600; font-size: 5.6px;
    color: var(--label); padding-left: 8px;
  }
  .cell {
    font-family: "Poppins", sans-serif; font-style: italic; font-size: 5.6px;
    line-height: 1.25; color: var(--cell); padding-right: 5px;
  }
</style>
</head>
<body>
<main class="poster">
  <div class="rink-backdrop" role="img" aria-label="Photo of an indoor ice rink with arena lights"></div>
  <div class="panel"></div>
  <div class="player player--left" role="img" aria-label="Photo of a female hockey player in a white jersey holding her stick"></div>
  <div class="player player--right" role="img" aria-label="Photo of a female hockey player in a blue jersey taking a shot"></div>

  <header class="title-band"><h1>HOCKEY HABITS OFFENSE</h1></header>

  <section class="habits habits--individual">
    <div class="grid head">
      <div class="tag tag--section">INDIVIDUAL</div>
      <div class="tag tag--average">AVERAGE</div>
      <div class="tag tag--good">GOOD</div>
      <div class="tag tag--great">GREAT</div>
    </div>
    <div class="rows">
      <div class="grid row"><span class="label">Compete</span><span class="cell">Watches during games and doesn't work hard in practice</span><span class="cell">Competes during games</span><span class="cell">Competes during games and practices</span></div>
      <div class="grid row"><span class="label">Mental Toughness</span><span class="cell">Gets easily upset with everyone</span><span class="cell">Park Mistakes (their's, teammates, referees)</span><span class="cell">Able to turn negative situations into positive energy and use it!</span></div>
      <div class="grid row"><span class="label">Spirit</span><span class="cell">ALL-IN when team is winning</span><span class="cell">ALL-IN during all games</span><span class="cell">ALL-IN during practice and games</span></div>
      <div class="grid row"><span class="label">Effort</span><span class="cell">Works hard when they want to</span><span class="cell">Works as hard as their opponents</span><span class="cell">Their effort matches the best of their ability - they give</span></div>
      <div class="grid row"><span class="label">Teamwork</span><span class="cell">They should get me the puck</span><span class="cell">I'll pass if I have to</span><span class="cell">Enjoys setting up their teammates for an easy goal as much as scoring!</span></div>
      <div class="grid row"><span class="label">Hockey IQ</span><span class="cell">Thinks they know hockey</span><span class="cell">Knows that they need to learn</span><span class="cell">Watches pro league, college, youth games trying to always learn</span></div>
    </div>
  </section>

  <section class="habits habits--with-puck">
    <div class="grid head">
      <div class="tag tag--section small">OFFENSE W/PUCK</div>
      <div class="tag tag--average">AVERAGE</div>
      <div class="tag tag--good">GOOD</div>
      <div class="tag tag--great">GREAT</div>
    </div>
    <div class="rows">
      <div class="grid row"><span class="label">Compete</span><span class="cell">Eyes always on the puck</span><span class="cell">Eyes on puck see game in peripheral vision</span><span class="cell">Eyes on the game peripheral vision for puck</span></div>
      <div class="grid row"><span class="label">Stickhandling</span><span class="cell">Control puck in front of body</span><span class="cell">Control puck side to side</span><span class="cell">Control puck in all positions</span></div>
      <div class="grid row"><span class="label">Making a Pass</span><span class="cell">Blindly hitting the puck</span><span class="cell">Making a pass toward teammate</span><span class="cell">Make a pass with eyes up tape to tape to where the player is going</span></div>
      <div class="grid row"><span class="label">Shooting</span><span class="cell">Shoots towards the net wherever they are</span><span class="cell">Shoots hard towards the net</span><span class="cell">Finds a good shooting lane and shoots as hard as they possibly can</span></div>
      <div class="grid row"><span class="label">Play making</span><span class="cell">Making a deke, pass or shot once D is on you</span><span class="cell">Making a deke, pass or shot before the D is on you</span><span class="cell">Anticipate the play and play in areas D can't get you</span></div>
    </div>
  </section>

  <section class="habits habits--without-puck">
    <div class="grid head">
      <div class="tag tag--section small">OFFENSE WO/PUCK</div>
      <div class="tag tag--average">AVERAGE</div>
      <div class="tag tag--good">GOOD</div>
      <div class="tag tag--great">GREAT</div>
    </div>
    <div class="rows">
      <div class="grid row row--tight"><span class="label">Receiving a Pass</span><span class="cell">Puck deflects off stick</span><span class="cell">Puck hits stick but body is in control</span><span class="cell">puck is controlled in a hockey position ready to make hockey play</span></div>
      <div class="grid row row--tight"><span class="label">Rebounds, tips, screens</span><span class="cell">Not in a good spot to get a rebound</span><span class="cell">In the area for a rebound</span><span class="cell">Constantly moving to find open ice and passing lanes</span></div>
      <div class="grid row row--tight"><span class="label">Finding open ice</span><span class="cell">Standing still covered</span><span class="cell">Standing still in open ice</span><span class="cell">Constantly moving to find open ice and passing lanes</span></div>
    </div>
  </section>
</main>
</body>
</html>
```